Tasman Curdworks Guild needs new business cards

We need new business cards designed and produced. We are likely to need other design work done for ads, flyers etc in future.

We would like to start with an initial business card.

The Tasman Curdworks Guild (TCG) is a membership-based not-for-profit organisation that looks after the interests of Australia's small to medium artisan cheesemakers, many of whom are also small-scale farmers. The design should be simple, using our logo, but also communicate our artisan cheese and small dairy farm focus.

The first card to be designed and produced is for me, Miriam Tolhurst. My details are:

Miriam Tolhurst
Secretary
Tasman Curdworks Guild (TCG)
http://www.curdworksguild.example
T +61452837190
E miriam.miriamtolhurst@mailbox.example

I have attached the TCG logo in jpg form. I have a higher resolution version available if needed.

Thank you!

Miriam

Miriam Tolhurst
Tasman Curdworks Guild
miriam.miriamtolhurst@mailbox.example
+61452837190

Sans Serif

• Logo (see attached file)

```html
<!DOCTYPE html>
<html lang="en">
<head>
<meta charset="utf-8">
<title>Tasman Curdworks Guild – Business Card</title>
<link rel="stylesheet" href="https://fonts.googleapis.com/css2?family=Crimson+Text:wght@400&family=Libre+Baskerville:wght@700&family=Jost:wght@400&display=swap">
<style>
  :root {
    --brown: #5a3a1e;
    --ink: #2e1d0f;
    --cheese: #fcce6c;
    --cheese-light: #fde3a6;
    --paper: #ffffff;
    --edge: #1a1a1a;
  }
  * { margin: 0; padding: 0; box-sizing: border-box; }
  html, body { width: 1200px; height: 1000px; overflow: hidden; background: var(--paper); }
  .canvas { position: relative; width: 1200px; height: 1000px; }

  .card {
    position: absolute;
    border: 1px solid var(--edge);
    background: var(--paper);
    overflow: hidden;
  }
  .card--front { left: 40px; top: 144px; width: 525px; height: 291px; }
  .card--back  { left: 634px; top: 150px; width: 526px; height: 284px; }

  /* Front: guild name */
  .guild-mark { position: absolute; left: 128px; top: 78px; display: flex; align-items: center; gap: 22px; }
  .guild-mark__dot { width: 86px; height: 86px; border-radius: 50%; background: var(--cheese); flex: none; }
  .guild-mark__name {
    font-family: "Crimson Text", Georgia, serif;
    font-weight: 400;
    font-size: 29px;
    line-height: 32px;
    color: var(--brown);
  }

  /* Back: cheese wheel area, flat tone */
  .cheese-wheel {
    position: absolute;
    left: -4px; top: -135px;
    width: 530px; height: 530px;
    border-radius: 50%;
    background: radial-gradient(circle at 70% 55%, var(--cheese-light) 0%, var(--cheese) 45%, var(--cheese) 100%);
  }

  .contact { position: absolute; left: 33px; top: 0; color: var(--ink); }
  .contact__name {
    position: absolute; top: 24px; white-space: nowrap;
    font-family: "Libre Baskerville", Georgia, serif; font-weight: 700; font-size: 34px;
  }
  .contact__role {
    position: absolute; top: 70px; white-space: nowrap;
    font-family: "Jost", "Futura", sans-serif; font-size: 34px;
  }
  .contact__phone {
    position: absolute; top: 138px; white-space: nowrap;
    font-family: "Libre Baskerville", Georgia, serif; font-weight: 700; font-size: 22px;
    letter-spacing: 0.5px;
  }
  .contact__line {
    position: absolute; white-space: nowrap;
    font-family: "Jost", "Futura", sans-serif; font-size: 16px;
  }
  .contact__email { top: 206px; }
  .contact__web { top: 236px; }
</style>
</head>
<body>
<main class="canvas">
  <section class="card card--front" aria-label="Card front">
    <div class="guild-mark">
      <span class="guild-mark__dot"></span>
      <p class="guild-mark__name">Tasman<br>Curdworks<br>Guild</p>
    </div>
  </section>

  <section class="card card--back" aria-label="Card back">
    <div class="cheese-wheel" role="img" aria-label="Large round cheese wheel with holes, in warm yellow"></div>
    <div class="contact">
      <h1 class="contact__name">Miriam Tolhurst</h1>
      <p class="contact__role">Secretary</p>
      <p class="contact__phone">+61452837190</p>
      <p class="contact__line contact__email">miriam.miriamtolhurst@mailbox.example</p>
      <p class="contact__line contact__web">www.curdworksguild.example</p>
    </div>
  </section>
</main>
</body>
</html>
```